Re-Brand of TindelMox along with a new website design

TindelMox Ltd are a software & database development company using technologies such as PHP, C#, HTML, JQuery, Flex, AS3, MySQL, Oracle, MSSQL. We like to target all types of business from small to large.

We are great at coding but rubbish at design so thats where we need your help!

We want a complete re-brand of TindelMox including logo, website design, and business cards.

We would like a design that is clean but other than that, please feel free to be creative.

****Logo****
We are looking for a logo that appears professional but with a splash of colour that indicates a creative side. Please see below some logos that we like the look of:

We like this one because it has a nice simple and clear font for the name of the company but also an icon which is colourful and stands out. http://markvault.example/2013/03/brivelo/

We like this one because it is very clean, simple and again very clear. http://markvault.example/2013/03/quantorels/

http://markvault.example/2013/03/tide-lamp/
http://markvault.example/2013/02/velmorin/
http://markvault.example/2013/01/art-gallery-tarnwick/

As you will see from all of these examples, the font is very clear but there is always a graphic representing the company too. This is what we like.

****Website****
These are some of the examples of websites we like:
https://www.zestrune.example/
https://www.chatterlane.example/home
http://www.haldenimagery.example/
http://www.vistor.example/
http://quillbay.example/
https://www.usebriefnest.example/personal-intros
http://www.marmotpanel.example/

The current site can be found at tindelmox.example.uk

Reason: We have extended the deadline of the project by 5 days as I realise the original deadline was very tight.

Software

Requirements
Must have
• Website must have the following pages
Home
Services
Projects
About Us
Contact Us

```html
<!DOCTYPE html>
<html lang="en">
<head>
<meta charset="utf-8">
<title>TindelMox — web, software, IT services</title>
<link rel="stylesheet" href="https://fonts.googleapis.com/css2?family=Questrial&family=Comfortaa:wght@300&display=swap">
<style>
  :root {
    --grey-band: #dedede;
    --mint: #36ffb6;
    --mint-deep: #2ef0c0;
    --ink: #333333;
    --paper: #f9f9f9;
    --card-dark: #282828;
    --crimson: #cc0644;
    --white: #ffffff;
    --line: #c9c9c9;
  }
  * { margin: 0; padding: 0; box-sizing: border-box; }
  html, body { width: 1200px; height: 1200px; overflow: hidden; }
  body {
    position: relative;
    background: var(--grey-band);
    font-family: "Questrial", sans-serif;
    color: var(--ink);
  }
  .hero {
    position: absolute; top: 122px; left: 0; width: 1200px; height: 473px;
    background: linear-gradient(180deg, var(--mint) 0%, var(--mint-deep) 100%);
  }
  .contact-bubble {
    position: absolute; left: 991px; top: 55px; width: 134px; height: 134px;
    border-radius: 50%; background: var(--white);
    border: 1px dashed var(--line);
    box-shadow: 0 1px 4px rgba(0,0,0,.18);
    display: flex; align-items: center; justify-content: center;
    font-size: 10px; letter-spacing: .5px; color: #222; text-decoration: none;
  }
  .brand-name {
    position: absolute; top: 110px; left: 0; width: 1200px; text-align: center;
    font-weight: normal; font-size: 80px; line-height: 1; color: #2e2e2e; letter-spacing: -1px;
  }
  .services-line {
    position: absolute; top: 299px; left: 0; width: 1200px; text-align: center;
    font-size: 14px; color: #333;
  }
  .services-line .sep { display: inline-block; width: 2px; height: 10px; background: #333; margin: 0 14px; vertical-align: -1px; }
  .intro {
    position: absolute; top: 351px; left: 443px; width: 285px; text-align: center;
    font-size: 10px; line-height: 11.7px; letter-spacing: .2px; color: #2c2c2c;
  }
  .intro p + p { margin-top: 11.7px; }
  .chat-line {
    position: absolute; top: 600px; left: 0; width: 1200px; text-align: center;
    font-size: 9.8px; letter-spacing: .4px; color: #222;
  }
  .projects {
    position: absolute; top: 660px; left: 0; width: 1200px; height: 303px;
    background: linear-gradient(160deg, var(--paper) 0%, #f2f2f2 100%);
    border-top: 1px dashed var(--line); border-bottom: 1px dashed var(--line);
  }
  .section-title {
    position: absolute; left: 0; width: 1200px; text-align: center;
    font-family: "Comfortaa", sans-serif; font-weight: 300;
  }
  .projects .section-title { top: 4px; font-size: 44px; color: #2f2f2f; letter-spacing: 1px; }
  .project-card {
    position: absolute; top: 65px; width: 218px; height: 218px;
    border: 1px solid #3a3a3a; background: var(--card-dark);
    box-shadow: 0 1px 3px rgba(0,0,0,.25);
  }
  .project-card .mark {
    height: 140px; background: var(--white);
    display: flex; align-items: center; justify-content: center;
    font-size: 26px; color: #222;
  }
  .project-card h3 { font-weight: normal; font-size: 9.4px; color: var(--white); padding: 11px 6px 0; letter-spacing: .4px; }
  .project-card p { font-size: 9.4px; line-height: 12.3px; letter-spacing: .3px; color: #dcdcdc; padding: 11px 6px 0; }
  .card-1 { left: 230px; } .card-2 { left: 486px; } .card-3 { left: 742px; }
  .arrow { position: absolute; }
  .what-we-do {
    position: absolute; top: 963px; left: 0; width: 1200px; height: 237px;
    background: var(--crimson); overflow: hidden;
  }
  .what-we-do .section-title {
    top: 18px; font-size: 48px; color: transparent;
    -webkit-text-stroke: 1px var(--white); letter-spacing: 2px;
  }
  .offer {
    position: absolute; top: 110px; width: 218px;
    font-size: 9.4px; line-height: 12.5px; letter-spacing: .3px; color: #f7d6e0;
  }
  .offer h3 { font-weight: normal; color: var(--white); font-size: 9.4px; letter-spacing: .4px; margin-bottom: 13px; }
  .offer p + p { margin-top: 12.5px; }
  .offer-1 { left: 234px; } .offer-2 { left: 490px; } .offer-3 { left: 746px; }
</style>
</head>
<body>
  <section class="hero">
    <h1 class="brand-name">TindelMox</h1>
    <div class="services-line">web<span class="sep"></span>sofware<span class="sep"></span>IT services</div>
    <div class="intro">
      <p>Based in Ipswich our clients are both local and national; large and small. You may be a start-up business in need of a ‘get me up and running quickly’ website, or a multi-million pound brand looking for an all singing, all dancing bespoke app.</p>
      <p>Maybe you are experiencing the pains and pleasures of growing your business and it’s time to improve your branding and to trade in your current home-spun website for something more professional.</p>
    </div>
  </section>
  <a class="contact-bubble" href="#contact">contact us</a>
  <p class="chat-line">Let’s chat today about where we can take your business.</p>

  <section class="projects">
    <h2 class="section-title">projects</h2>
    <svg class="arrow" style="left:118px;top:140px" width="28" height="52" viewBox="0 0 28 52"><polyline points="26,1 2,26 26,51" fill="none" stroke="#aaa" stroke-width="1"/></svg>
    <svg class="arrow" style="left:1044px;top:140px" width="28" height="52" viewBox="0 0 28 52"><polyline points="2,1 26,26 2,51" fill="none" stroke="#aaa" stroke-width="1"/></svg>
    <article class="project-card card-1">
      <div class="mark">Crewtrack Pro</div>
      <h3>Crewtrack Pro</h3>
      <p>Crewtrack Pro allows your business to view the location of your staff via a web portal or mobile phone.</p>
    </article>
    <article class="project-card card-2">
      <div class="mark">Wayfold</div>
      <h3>Wayfold</h3>
      <p>Wayfold is a system that allows conscientious parents to view the location of their child via the web and mobile phone.</p>
    </article>
    <article class="project-card card-3">
      <div class="mark">Postboard Free</div>
      <h3>Postboard Free</h3>
      <p>PostboardFree is a system that allows you to place adverts onto the website and sell their items absolutely free.</p>
    </article>
  </section>

  <section class="what-we-do">
    <h2 class="section-title">What we do...</h2>
    <svg class="arrow" style="left:118px;top:182px" width="28" height="52" viewBox="0 0 28 52"><polyline points="26,1 2,26 26,51" fill="none" stroke="#f0a9bf" stroke-width="1"/></svg>
    <svg class="arrow" style="left:1044px;top:182px" width="28" height="52" viewBox="0 0 28 52"><polyline points="2,1 26,26 2,51" fill="none" stroke="#f0a9bf" stroke-width="1"/></svg>
    <div class="offer offer-1">
      <h3>Website Design and Development</h3>
      <p>Your website is a representation of who you are or what your business stands for.</p>
      <p>If you feel your website could better show off who you are and what you do TindelMox is the right team for you.</p>
      <p>You will work with a team that will find out exactly what you need.</p>
    </div>
    <div class="offer offer-2">
      <h3>Rich Internet Applications</h3>
      <p>You may be asking yourself, “what the heck is a Rich Internet Application..?” The chances are you play with one every day. If you have ever used Nimbus Sheets then you know what we are talking about.</p>
      <p>A Rich Internet Application is all about offering your clients a more engaging and immersive experience.</p>
    </div>
    <div class="offer offer-3">
      <h3>Mobile &amp; Tablet Applications</h3>
      <p>If you are sitting on the next great idea for a mobile or tablet app TindelMox has all the experience you need.</p>
      <p>You will work with a team who are able to get your idea onto all of the major mobile platforms including Phonix, Slatepad, Droidra and Paneos.</p>
    </div>
  </section>
</body>
</html>
```